Pivora has a great new logo - now we need a website!!

Pivora has been in business for a long time and needs to start a new era. Additional to other changes being made in the business itself, Pivora needs an overhaul of its entire branding. PART 1 is COMPLETE - we have our new logo!

Next step... new website! That's where you come in.

Pivora provides a range of computer related services including computer maintenance, networking, sales & cloud services. We provide onsite (field) and remote support. Our customers range from homes to companies with 100+ computers. We pride ourselves on clear and honest communication.

We are a small business but want a professional yet easy-going look that shows the 'cool' side of having your computer system cared for. The website should exude trustworthiness and professionalism but still get comments like 'modern' and 'smart design'. We want our customers to feel that choosing any other company to maintain their system would be a 'geeky' choice.

We like clear thinking so an uncluttered, well organised structure is appreciated. Obvious references to calling or emailing us would be good so people dont need to search around for our contact details.

We look after both Quince & Veltharon operating systems so there needs to be universal appeal rather than a look associated with only one of these two brands.

We want to wow our current clients but also attract new ones so a focus on SEO is a must. And a focus on social media too with links/feeds to Chatterly, chirpex and WorkLoop!

Have a look at www.pivora.com.au so you can see for yourself how much you can help us!

**Breathe new life into Pivora's online presence!**

(We do have a separate website www.kelbrohome.com.au that we set as the homepage for our clients - we like how it is but it might need freshening up to match our new site. We will also want our chatterly page totally made over. You'll probably have other suggestions of things we should be doing. We want to form an ongoing relationship with the right designer!)

(Also, we are open to suggestions regarding the logo size and colour)
Updates

I dont want to cramp anyones creativity but i like this: http://www.quindlework.com/demo/themes/wordpress/2011/saffron/

I'm obivously happy to see your own ideas too!

I also like this one: http://marbleloft.net/item/dralo-responsive-wordpress-theme/7184206

Clarification: We are looking for a working, implemented website, not just design of the theme. Once the general page layout is done we can do the majority of the content input. But we do want a workable shell with images.

We are open to buying existing themes if that helps. Thanks!

Site also needs email contact form, testimonial submission page, blog (feed to home page), chatterly like button

Reason: I haven't found the ideal one yet... We want some other designers to send their ideas.

Reason: We need a little more time to make our decision.

Target Market(s)

Mainly small to medium businesses but also homes

Industry/Entity Type

Small Business

Requirements
Must have
• SEO
Social Media
That little address bar icon
R in a circle at the bottom of the site to show we have trademarked our company name
A finished product website with content and images that we can modify ourselves over time.

```html
<!DOCTYPE html>
<html lang="en">
<head>
<meta charset="utf-8">
<title>Pivora IT Solutions &amp; Support</title>
<link rel="stylesheet" href="https://fonts.googleapis.com/css2?family=Cabin:wght@400;500;600;700&family=Open+Sans:ital,wght@0,400;0,600;1,400&display=swap">
<style>
:root{
  --band:#5a6aa2;
  --band-top:#4e5d95;
  --page:#ebebeb;
  --white:#ffffff;
  --ink:#2a2a2a;
  --body:#555555;
  --accent:#56659a;
  --dot:#8a94bb;
  --dark:#222222;
  --footer:#5d6da9;
  --footer-text:#e4e8f5;
  --field:#a9b3dc;
  --rule:#d6d6d6;
}
*{margin:0;padding:0;box-sizing:border-box}
html,body{width:1200px;height:1196px;overflow:hidden}
body{position:relative;background:var(--page);font-family:"Open Sans",sans-serif;color:var(--body)}
.abs{position:absolute}
.top-band{left:0;top:0;width:1200px;height:92px;background:linear-gradient(var(--band-top),var(--band))}
.phone{left:852px;top:14px;display:flex;align-items:center;gap:12px;color:var(--white);font-family:"Cabin",sans-serif;font-size:27px}
.brand{left:130px;top:43px;width:256px;height:91px;background:linear-gradient(#fff,#e9e9e9);box-shadow:0 1px 4px rgba(0,0,0,.35);display:flex;align-items:center;gap:14px;padding-left:18px}
.brand-mark{width:52px;height:52px;border-radius:50%;background:var(--ink)}
.brand-name{font-family:"Cabin",sans-serif;font-weight:700;font-size:30px;color:var(--ink)}
.nav{left:450px;top:67px;width:620px;height:50px;background:#2b2b2b;border-radius:4px;display:flex;justify-content:space-around;align-items:center;padding:0 6px}
.nav a{color:var(--white);text-decoration:none;font-size:13px}
.hero-title{left:130px;top:184px;font-family:"Cabin",sans-serif;font-weight:600;font-size:25px;color:var(--ink)}
.hero-quote{left:130px;top:219px;width:360px;font-family:"Cabin",sans-serif;font-weight:500;font-size:25px;line-height:33px;color:var(--accent)}
.btn{background:var(--dark);color:var(--white);border-radius:3px;display:flex;align-items:center;justify-content:center;font-family:"Cabin",sans-serif}
.learn{left:130px;top:316px;width:140px;height:34px;font-size:17px;font-weight:500}
.dots{left:130px;top:451px;display:flex;gap:4px}
.dots span{width:21px;height:21px;border-radius:50%;background:var(--dot)}
.dots span:first-child{background:#4f5d94}
.hero-frame{left:530px;top:190px;width:460px;height:290px;background:var(--white);padding:5px;box-shadow:0 8px 10px -6px rgba(0,0,0,.45)}
.hero-photo{width:100%;height:100%;background:radial-gradient(circle at 45% 55%,#3a3029,#111 60%)}
.content{left:0;top:518px;width:1200px;height:396px;background:var(--white)}
.col{top:541px;width:300px;height:330px}
.col h2{position:absolute;left:0;top:0;font-family:"Cabin",sans-serif;font-weight:400;font-size:25px;color:var(--accent)}
.thumb{position:absolute;left:0;top:42px;width:300px;height:135px;border-radius:3px}
.col p{position:absolute;left:0;top:188px;width:300px;font-size:12.5px;line-height:23px;color:var(--body)}
.col .btn{position:absolute;left:0;top:298px;width:89px;height:27px;font-size:14px;font-family:"Open Sans",sans-serif}
.service{position:absolute;left:0;width:300px;padding-left:82px;font-size:12.5px;line-height:23px}
.service b{font-family:"Cabin",sans-serif;font-weight:600;font-size:14px;color:var(--ink)}
.service a,.news a{color:var(--accent);text-decoration:none}
.service svg{position:absolute;left:0}
.rule{left:130px;top:892px;width:940px;height:8px;background:var(--rule)}
.footer{left:0;top:914px;width:1200px;height:282px;background:var(--footer);color:var(--footer-text)}
.footer h3{position:absolute;top:20px;font-family:"Cabin",sans-serif;font-weight:400;font-size:20px;color:var(--white)}
.news{position:absolute;left:130px;top:52px;width:300px;font-size:12px;line-height:18px}
.news a{color:#111}
.news .date{font-weight:600;color:var(--white);margin:9px 0 10px}
.news hr{border:0;border-top:1px solid #7d8bbf;margin-bottom:8px}
.links{position:absolute;left:481px;top:46px;list-style:none;font-size:12px}
.links li{height:25.2px;display:flex;align-items:center;gap:14px}
.links li::before{content:"\2192";font-size:10px}
.social{position:absolute;left:689px;top:50px;list-style:none;font-size:12.5px}
.social li{height:35px;display:flex;align-items:center;gap:8px}
.social i{width:16px;height:16px;border-radius:2px;background:#dfe4f4;display:block}
.email{position:absolute;left:877px;top:54px;width:193px;height:30px;background:var(--field);border-radius:3px;padding-left:11px;display:flex;align-items:center;font-style:italic;font-size:12.5px;color:#4e5b8c}
.go{position:absolute;left:1025px;top:96px;width:45px;height:30px;font-size:15px;font-weight:700}
.foot-brand{position:absolute;left:850px;top:163px;display:flex;align-items:center;gap:8px}
.foot-brand span{width:50px;height:50px;border-radius:50%;background:var(--white)}
.foot-brand b{font-family:"Cabin",sans-serif;font-size:22px;font-weight:700;color:var(--white)}
.copy{position:absolute;left:851px;top:224px;font-size:11px;color:var(--white)}
</style>
</head>
<body>
<div class="abs top-band"></div>
<div class="abs phone">
  <svg width="33" height="24" viewBox="0 0 33 24" aria-hidden="true"><path d="M2 7C2 2 31 2 31 7v3h-8V7H10v3H2z M7 12h19l4 11H3z" fill="#fff"/><circle cx="16.5" cy="17" r="3.6" fill="#56659a"/></svg>
  <span>(03) 94176208</span>
</div>
<div class="abs brand"><span class="brand-mark"></span><span class="brand-name">PIVORA</span></div>
<nav class="abs nav"><a>Home</a><a>Services</a><a>Pricing</a><a>Opening Hours</a><a>Pay Bill</a><a>Links</a><a>Contact Us</a></nav>

<h1 class="abs hero-title">I.T. PROBLEMS FIXED FAST</h1>
<p class="abs hero-quote">"One call to Pivora could help solve it all."</p>
<div class="abs btn learn">Learn More</div>
<div class="abs dots"><span></span><span></span><span></span><span></span></div>
<div class="abs hero-frame"><div class="hero-photo" role="img" aria-label="Hand touching an information technology diagram on a dark background"></div></div>

<div class="abs content"></div>
<section class="abs col" style="left:130px">
  <h2>Welcome to Our Site</h2>
  <div class="thumb" role="img" aria-label="Smiling business team" style="background:linear-gradient(90deg,#3a3a3f,#8b8680 55%,#e6e6e6)"></div>
  <p>At Pivora, we provide a range of computer related services. From new computers to website design &amp; hosting, we can help you with almost any techno-logical need....</p>
  <div class="btn">Read More</div>
</section>
<section class="abs col" style="left:450px">
  <h2>What We Do</h2>
  <div class="thumb" role="img" aria-label="Hand drawing colourful swirls on a screen" style="background:linear-gradient(90deg,#e9f0f5,#5a86a8 45%,#c9b8a8 80%,#f1f1f1)"></div>
  <p>Troubleshooting Computer Sales Networking Hard-ware Repairs Virus Removal Offsite Backup Internet Connections Website Hosting Exchange Email Remote Access...</p>
  <div class="btn">Read More</div>
</section>
<section class="abs col" style="left:770px">
  <h2>Services</h2>
  <div class="service" style="top:36px">
    <svg width="58" height="58" viewBox="0 0 58 58" aria-hidden="true" fill="none" stroke="#3d4a7c" stroke-width="3" style="top:8px"><circle cx="29" cy="29" r="27"/><ellipse cx="29" cy="29" rx="12" ry="27"/><path d="M29 2v54M2 29h54M6 16h46M6 42h46"/></svg>
    <b>Support :</b> Pivora provides onsite and remote support to both homes and businesses...<a>More</a>
  </div>
  <div class="service" style="top:119px">
    <svg width="58" height="58" viewBox="0 0 58 58" aria-hidden="true" style="top:6px"><path d="M2 34l9-7 11 12L52 4l4 4-34 48z" fill="#3d4a7c"/></svg>
    <b>Sales :</b> If you are after a new desktop, laptop, server or any computer acces-sory or software..<a>More</a>
  </div>
  <div class="service" style="top:199px">
    <svg width="58" height="64" viewBox="0 0 58 64" aria-hidden="true" fill="#3d4a7c" style="top:2px"><circle cx="34" cy="7" r="7"/><path d="M16 26h20l-9 30c4 0 7-3 9-6l2 2c-4 8-10 12-17 12-6 0-8-4-6-10l7-23h-7z"/></svg>
    <b>Internet Services:</b> If you are after quality web hosting provided by Australian servers, Pivora has com-petitive plans on offer...<a>More</a>
  </div>
  <div class="btn">Read More</div>
</section>
<div class="abs rule"></div>

<footer class="abs footer">
  <h3 style="left:130px">Latest News</h3>
  <div class="news">
    <p>Lorem ipsum dolor sit amet, consectetur adipiscing elit. Fusce accumsan, elit a suscipit sagittis, tortor sapien cursus risus....<a>More</a></p>
    <p class="date">Nov 10, 2012</p>
    <hr>
    <p>Lorem ipsum dolor sit amet, consectetur adipiscing elit. Fusce accumsan, elit a suscipit sagittis, tortor sapien cursus risus....<a>More</a></p>
    <p class="date">Nov 11 2012</p>
  </div>
  <h3 style="left:481px">Company</h3>
  <ul class="links"><li>Home</li><li>Services</li><li>Pricing</li><li>Opening Hours</li><li>Pay Bills</li><li>Links</li><li>Contact Us</li></ul>
  <h3 style="left:689px">Connect us</h3>
  <ul class="social"><li><i></i>Chatterly</li><li><i></i>Chirpex</li><li><i></i>WorkLoop</li><li><i></i>Rss Feed</li></ul>
  <h3 style="left:878px">Newsletter Sign Up</h3>
  <div class="email">email address</div>
  <div class="btn go">GO</div>
  <div class="foot-brand"><span></span><b>PIVORA</b></div>
  <p class="copy">©2012. All Right Reserved | Privacy Policy</p>
</footer>
</body>
</html>
```